Corvane Project Services - Flyer

Project Breif:
I need a single page A4 Capability Statement, which will be used to market our services to prospective clients, both in print and via email PDF.
It needs to look professional and should incorporate the elements I have uploaded into files, these include:
Capability Statement Text
Corvane Services Company Logo
Additional Logo’s (Tools We Use)
Glimmer Bay Pics can be cut into the page
I have included examples of capability statements as a guide to what i am looking for.
Regards
Derek
Engineering Consulting

```html
<!DOCTYPE html>
<html lang="en">
<head>
<meta charset="utf-8">
<title>Corvane Project Services – Capability Statement</title>
<link rel="stylesheet" href="https://fonts.googleapis.com/css2?family=Montserrat:wght@400;500;600;700;800&family=Raleway:wght@400;500;600;700&display=swap">
<style>
  :root {
    --blue: #4a90d0;
    --blue-deep: #3a7cc0;
    --blue-light: #6aaee0;
    --sky: #8ccbea;
    --ink: #1c1c1c;
    --text: #2a2a2a;
    --grey-soft: #e4e6e9;
    --rule: #5a95cf;
    --white: #ffffff;
    --page-bg: #ffffff;
  }
  * { box-sizing: border-box; margin: 0; padding: 0; }
  html, body { width: 880px; height: 1200px; overflow: hidden; background: var(--page-bg); }
  body { font-family: "Raleway", sans-serif; color: var(--text); }

  .sheet { position: relative; width: 880px; height: 1200px; background: var(--white); overflow: hidden; }
  .top-band { position: absolute; left: 0; top: 0; width: 100%; height: 10px; background: var(--sky); }

  /* brand */
  .brand { position: absolute; left: 40px; top: 30px; width: 240px; text-align: center; }
  .brand-mark { display: block; margin: 0 auto 10px; width: 70px; height: 70px; border-radius: 50%; background: var(--blue); }
  .brand-name { font-family: "Raleway", sans-serif; font-weight: 700; color: var(--ink); font-size: 19px; letter-spacing: 0.5px; line-height: 1.1; }
  .brand-sub { font-family: "Raleway", sans-serif; font-weight: 700; color: var(--ink); font-size: 13px; letter-spacing: 7px; margin-top: 3px; }

  /* title */
  .doc-title { position: absolute; right: 38px; top: 52px; text-align: right; }
  .doc-title .lead { font-family: "Montserrat", sans-serif; font-weight: 800; font-size: 64px; line-height: 1; color: var(--blue); letter-spacing: -0.5px; }
  .doc-title .tail { font-family: "Montserrat", sans-serif; font-weight: 400; font-size: 40px; line-height: 1; color: var(--ink); letter-spacing: 15px; margin-top: 6px; margin-right: -15px; }

  /* hero photos */
  .hero { position: absolute; left: 5px; top: 188px; width: 871px; height: 273px; }

  /* intro column */
  .intro-head { position: absolute; left: 34px; top: 480px; width: 411px; }
  .intro-head h1 { font-family: "Montserrat", sans-serif; font-weight: 800; font-size: 34px; line-height: 1.0; color: var(--blue); }
  .intro-head .tagline { font-family: "Montserrat", sans-serif; font-weight: 500; font-size: 18px; line-height: 1.2; color: var(--blue-light); margin-top: 9px; text-transform: uppercase; }
  .intro-head .short-rule { width: 62px; height: 2px; background: var(--ink); margin-top: 8px; }

  .intro-body { position: absolute; left: 34px; top: 640px; width: 411px; }
  .intro-body p { font-size: 14px; line-height: 18.5px; text-align: justify; margin-bottom: 8px; color: var(--text); }

  .goal { position: absolute; left: 9px; top: 822px; width: 436px; height: 128px; border-radius: 0 14px 14px 0;
          background: linear-gradient(180deg, var(--blue-light) 0%, var(--sky) 100%); color: var(--white); padding: 10px 0 0 26px; }
  .goal h2 { font-family: "Montserrat", sans-serif; font-weight: 800; font-size: 56px; line-height: 1; letter-spacing: -1px; }
  .goal p { font-size: 19px; line-height: 23px; margin-top: 10px; white-space: nowrap; }

  .divider { position: absolute; left: 476px; top: 484px; width: 1px; height: 490px; background: var(--grey-soft); }

  /* services */
  .services { position: absolute; left: 498px; top: 480px; width: 346px; }
  .services h2 { font-family: "Montserrat", sans-serif; font-weight: 800; font-size: 35px; color: var(--grey-soft); line-height: 1; letter-spacing: -0.5px; white-space: nowrap; margin-bottom: 26px; }
  .service-group { margin-bottom: 14px; }
  .service-group h3 { display: flex; align-items: center; font-family: "Raleway", sans-serif; font-weight: 700; font-size: 17px; line-height: 22px; color: var(--blue); margin-bottom: 6px; white-space: nowrap; }
  .service-group h3::after { content: ""; flex: 1; height: 1px; background: var(--rule); margin-left: 8px; }
  .service-list { list-style: none; }
  .service-list li { position: relative; padding-left: 22px; font-size: 14.5px; line-height: 19.5px; color: var(--text); white-space: nowrap; }
  .service-list li::before { content: ""; position: absolute; left: 2px; top: 5px; width: 10px; height: 10px; border-radius: 50%; background: var(--blue-light); }
  .service-list li::after { content: ""; position: absolute; left: 5px; top: 7px; width: 3px; height: 5px; border: solid var(--white); border-width: 0 1.5px 1.5px 0; transform: rotate(45deg); }

  /* tools */
  .tools { position: absolute; left: 0; top: 1002px; width: 100%; }
  .tool-row { display: flex; justify-content: center; align-items: center; gap: 46px; height: 44px; }
  .tool-row + .tool-row { margin-top: 20px; height: 32px; }
  .tool { display: flex; align-items: center; gap: 8px; font-family: "Raleway", sans-serif; font-weight: 700; font-size: 19px; white-space: nowrap; }
  .tool .chip { width: 22px; height: 22px; }
  .tool .dot { width: 22px; height: 22px; border-radius: 50%; }
  .t-red { color: #c8281e; }
  .t-green { color: #1e8a3c; } .t-green .chip { background: #1e8a3c; }
  .t-ink { color: var(--ink); } .t-ink .chip { background: #d93a2f; }
  .t-maroon { color: #b02432; }
  .t-teal { color: #1a5a73; } .t-teal .dot { background: #1a5a73; }
  .t-blue { color: var(--blue-deep); }

  /* footer */
  .footer { position: absolute; left: 0; top: 1123px; width: 100%; height: 77px; background: var(--blue); color: var(--white); text-align: center; padding-top: 12px; }
  .footer .contact-name { font-family: "Montserrat", sans-serif; font-weight: 800; font-size: 25px; }
  .footer .contact-role { font-family: "Raleway", sans-serif; font-weight: 500; font-size: 14px; }
  .contact-line { display: flex; justify-content: center; gap: 24px; margin-top: 8px; font-size: 16px; font-weight: 500; }
  .contact-line span { display: inline-flex; align-items: center; gap: 8px; }
  .contact-line svg { width: 16px; height: 16px; }
</style>
</head>
<body>
<div class="sheet">
  <div class="top-band"></div>

  <header class="brand">
    <span class="brand-mark"></span>
    <div class="brand-name">CORVANE PROJECT</div>
    <div class="brand-sub">SERVICES</div>
  </header>

  <div class="doc-title">
    <div class="lead">CAPABILITY</div>
    <div class="tail">STATEMENT</div>
  </div>

  <svg class="hero" viewBox="0 0 871 273" preserveAspectRatio="none">
    <defs>
      <linearGradient id="ganttTone" x1="0" y1="0" x2="1" y2="1">
        <stop offset="0" stop-color="#eef2f7"/>
        <stop offset="1" stop-color="#cdd9e8"/>
      </linearGradient>
      <linearGradient id="meetingTone" x1="0" y1="0" x2="1" y2="1">
        <stop offset="0" stop-color="#dfe8f1"/>
        <stop offset="1" stop-color="#b8cde0"/>
      </linearGradient>
    </defs>
    <polygon points="0,0 424,0 506,273 0,273" fill="url(#ganttTone)" role="img" aria-label="Photo of a printed Gantt chart schedule with a pen"/>
    <polygon points="434,0 871,0 871,273 516,273" fill="url(#meetingTone)" role="img" aria-label="Photo of colleagues reviewing report papers at a desk"/>
  </svg>

  <section class="intro-head">
    <h1>CORVANE PROJECT SERVICES LTD.</h1>
    <div class="tagline">Is a leading project control consultancy based in Co Cork Ireland</div>
    <div class="short-rule"></div>
  </section>

  <section class="intro-body">
    <p>For over 20 years we havebeen helping our clients to deliver complex projects and programs throughout mainland Europe.</p>
    <p>We are passionate about empower organisations to achieve their objectives, on time and on budget.</p>
    <p>We are continually innovating, evolving and learning, utilize the latest industry tools and techniques to deliver real value to our clients.</p>
  </section>

  <div class="goal">
    <h2>OURGOAL</h2>
    <p>is to make successful project delivery<br>more achievable and repeatable.</p>
  </div>

  <div class="divider"></div>

  <section class="services">
    <h2>CORE SERVICES</h2>
    <div class="service-group">
      <h3>Planning and Scheduling</h3>
      <ul class="service-list">
        <li>Tender Planning</li>
        <li>Interactive Planning / Pull Planning</li>
        <li>EPCMV Planning &amp; Scheduling</li>
        <li>Schedule Earned Value Management</li>
        <li>Independent Schedule Quality Assessment</li>
        <li>Schedule Risk Analysis (Monte Carlo)</li>
        <li>Training</li>
      </ul>
    </div>
    <div class="service-group">
      <h3>Management of Risk</h3>
      <ul class="service-list">
        <li>Risk Management Policies &amp; Procedures</li>
        <li>Risk Management Strategy</li>
        <li>Risk Registers</li>
        <li>Risk Improvement Planning</li>
        <li>Risk Response and Communication</li>
        <li>Risk Management Training</li>
      </ul>
    </div>
    <div class="service-group">
      <h3>Cost Control</h3>
      <ul class="service-list">
        <li>Estimating &amp; Forecasting</li>
        <li>Earned Value Analysis</li>
        <li>Progress Reporting</li>
        <li>Cost Risk Analysis</li>
      </ul>
    </div>
  </section>

  <section class="tools">
    <div class="tool-row">
      <div class="tool t-red">Ledgerline Planner</div>
      <div class="tool t-green"><span class="chip"></span>Taskframe</div>
      <div class="tool t-ink"><span class="chip"></span>Ostra Planner</div>
      <div class="tool t-maroon">Waypoint Pro</div>
    </div>
    <div class="tool-row">
      <div class="tool t-teal"><span class="dot"></span>RiskMethod</div>
      <div class="tool t-blue">Kestrel Metrics</div>
    </div>
  </section>

  <footer class="footer">
    <div><span class="contact-name">DEREK HALLORAN</span> <span class="contact-role">(MANAGING DIRECTOR)</span></div>
    <div class="contact-line">
      <span>
        <svg viewBox="0 0 16 16"><circle cx="8" cy="8" r="8" fill="#fff"/><rect x="4" y="5" width="8" height="6" fill="none" stroke="#4a90d0" stroke-width="1.2"/><path d="M4 5 L8 8.5 L12 5" fill="none" stroke="#4a90d0" stroke-width="1.2"/></svg>
        INFO@CORVANESERVICES.IE
      </span>
      <span>
        <svg viewBox="0 0 16 16"><circle cx="8" cy="8" r="8" fill="#fff"/><circle cx="8" cy="8" r="4.5" fill="none" stroke="#4a90d0" stroke-width="1.1"/><ellipse cx="8" cy="8" rx="2" ry="4.5" fill="none" stroke="#4a90d0" stroke-width="1"/><path d="M3.5 8 H12.5" stroke="#4a90d0" stroke-width="1"/></svg>
        WWW.CORVANESERVICES.IE
      </span>
      <span>
        <svg viewBox="0 0 16 16"><circle cx="8" cy="8" r="8" fill="#fff"/><path d="M5.5 4.5 L7 4.5 L7.6 6.6 L6.7 7.3 Q7.6 9 8.9 9.5 L9.6 8.7 L11.5 9.3 L11.5 10.8 Q9 11.6 6.6 9.3 Q4.6 7 5.5 4.5 Z" fill="#4a90d0"/></svg>
        +353 (0)871459620
      </span>
    </div>
  </footer>
</div>
</body>
</html>
```